Fatigued and Overloaded by COVID Messages? We need original illustrations to show that.

Everywhere you look there are messages about COVID. That is leading many people to feel fatigued and overloaded by the messages.

We surveyed U.S. adults March 20th - 24th, 2020 and measured message fatigue, information overload, perceived repetition, and perceived exaggeration. Here is how participants responded:

When it comes to coronavirus . . .
55% feel exhausted by all the messages.
54% feel overloaded by the amount of information.
51% feel that the messages are repetitive.
47% feel like messages exaggerate how bad it is.

In other words, almost half of U.S. adults show signs of message fatigue, information overload, perceived message repetition, and perceived message exaggeration.

We will continue to survey 400 adults every week for the next 16 weeks. Each time we will measure message fatigue, information overload, perceived repetition, and perceived exaggeration. We expect that it will increase over time.

What are we looking for? We need innovative and original illustrations that attempt to communicate these findings. The illustrations would visualize message fatigue, information overload, perceived message repetition, and perceived message exaggeration.

What sort of visual are we looking for? Our preference is for an original illustration (or set of illustrations). Our preference is for creative and powerful illustrations, but we are also open to the creative and well-executed infographics.

We need these images fast . We will award monetary prizes to the 3 best designs. If we like more than that, then we might purchase more (e.g., in past contests, we have purchased as many as 30 designs).

What we will need:
(1) The illustrations must be original and we will need the photoshop and/or illustrator files for all artwork. (By original, we mean that the illustrations are 100% created by you. Our organization requires that we utilize only original illustrated work. We have had issues with free imagery being pirated and reposted as free. We sidestep that issue by just having everything created.)

(2) The illustration should say, somewhere: "Based on a survey of 400 U.S. adults conducted March 20 - 24th, 2020."

(3) We will have almost 4 months worth of data by the time this is done. In other words, the illustrations might be able to help us present that weekly data.

(4) We have conducted other Artvendo projects. It might be helpful to examine designs we liked in the past. For example, here is another COVID project we just finished:

https://jobs.artvendo-example.com/job/5162048

Target Market(s)

U.S. adults

Requirements
Must have
• Original illustrations. Mobile friendly design. People will view this on their smartphones.
Nice to have
• A design that we can use to communicate the data across time.

```html
<!DOCTYPE html>
<html lang="en">
<head>
<meta charset="utf-8">
<title>COVID Message Fatigue</title>
<link href="https://fonts.googleapis.com/css2?family=Poppins:wght@500&family=Source+Sans+3:wght@400&display=swap" rel="stylesheet">
<style>
  :root {
    --bg-deep: #6a2a6c;
    --bg-light: #6f74b2;
    --band: rgba(224, 220, 240, 0.78);
    --coral: #f75254;
    --white: #ffffff;
    --ink: #111111;
    --bar-glass: rgba(245, 240, 242, 0.78);
    --art-dark: #021b27;
    --art-skin: #c4928a;
    --art-brown: #80583f;
  }
  * { box-sizing: border-box; margin: 0; padding: 0; }
  html, body { width: 960px; height: 1200px; overflow: hidden; }
  body {
    position: relative;
    background: linear-gradient(200deg, var(--bg-light) 0%, #5f4c8f 45%, var(--bg-deep) 100%);
    font-family: "Source Sans 3", "Myriad Pro", sans-serif;
  }
  .scene-art {
    position: absolute; left: 0; top: 495px; width: 960px; height: 705px;
    background: linear-gradient(160deg, var(--art-dark) 0%, var(--art-dark) 30%, var(--art-skin) 55%, var(--art-dark) 75%, var(--art-brown) 100%);
    border-radius: 420px 360px 0 0;
    opacity: 0.95;
  }
  .intro-band {
    position: absolute; left: 2px; top: 71px; width: 958px; height: 94px;
    background: var(--band);
    display: flex; align-items: center; justify-content: center;
    text-align: center; color: var(--ink);
    font-size: 24px; line-height: 29px;
  }
  .title-pill {
    position: absolute; left: 2px; top: 207px; width: 958px; height: 191px;
    background: var(--white); border-radius: 96px;
    display: flex; align-items: center; justify-content: center;
    text-align: center; color: var(--coral);
  }
  .title-text { font-weight: 400; font-size: 38px; line-height: 46px; }
  .stat {
    position: absolute; left: 40px; width: 799px; height: 81px;
    border: 1.5px solid var(--coral); border-radius: 41px;
    background: var(--bar-glass);
  }
  .stat-label {
    position: absolute; left: -1.5px; top: -1.5px; height: 81px;
    background: var(--coral); border-radius: 41px;
    display: flex; align-items: center; justify-content: center;
    text-align: center; color: var(--white);
    font-family: "Poppins", sans-serif; font-weight: 500;
    font-size: 23px; line-height: 28px; letter-spacing: 0.3px;
  }
  .stat-value {
    position: absolute; top: 0; height: 78px;
    display: flex; align-items: center;
    color: var(--coral);
    font-family: "Poppins", sans-serif; font-weight: 500; font-size: 34px;
  }
  .source-note {
    position: absolute; left: 0; width: 960px; top: 1139px;
    text-align: center; color: var(--white); font-size: 25px; line-height: 30px;
  }
</style>
</head>
<body>
  <div class="scene-art" role="img" aria-label="Illustration of a tired woman with dark hair resting her head on her arm"></div>

  <div class="intro-band">
    <p>Everywhere you look there are messages about COVID. That is leading<br>many people to feel fatigued and overloaded by the messages.</p>
  </div>

  <div class="title-pill">
    <h1 class="title-text">Percentage of U.S. adults that measured<br>message fatigue, information overload, perceived<br>repetition, and perceived exaggeration</h1>
  </div>

  <div class="stat" style="top:558px">
    <div class="stat-label" style="width:439px">Feel exhausted by<br>all the messages</div>
    <div class="stat-value" style="left:474px">55%</div>
  </div>
  <div class="stat" style="top:672px">
    <div class="stat-label" style="width:431px">Feel overloaded by the<br>amount of information</div>
    <div class="stat-value" style="left:466px">54%</div>
  </div>
  <div class="stat" style="top:784px">
    <div class="stat-label" style="width:407px">Feel that the<br>messages are repetitive</div>
    <div class="stat-value" style="left:442px">51%</div>
  </div>
  <div class="stat" style="top:897px">
    <div class="stat-label" style="width:375px">Feel like messages<br>exaggerate how bad it is</div>
    <div class="stat-value" style="left:410px">47%</div>
  </div>

  <p class="source-note">Based on a survey of 400 U.S. adults conducted March 20 - 24th, 2020.</p>
</body>
</html>
```